Design AND code an HTML landing page

A landing page for campaigns and webinars respondents for project www.brevamor-homes.example. We expect the design to be coded. We will provide the copy and content. It will be a simple landing page for a new development project, to capture details of any potential clients showing interest, including any leads generated via webinars.

Broad instructions are as follows:
- It should not have a header or footer. Minimum escape links as possible.
- Create a lead generator box to get e-mails / relevant info of people interested.
- If possible, add a virtual tour (link to host server provided) at the top of the page.
- Content will be provided
- An option to include a link to a ClipVerra video

Target Market(s)

Pre/retiree and retirees

Industry/Entity Type

Real estate development, retirement, relocation, travel and tourism

Coding

Coded - Design and coding required

Font styles to use
Other font styles liked:
• Preferably same as existing site

Colors
FFF300
FFF600
FEFA6F
FFFEC7
FFFEE8

Requirements
Must have
• Simple yet appealing look and feel, within the motif of the project, simple list of questions
Should not have
• Emojis, unrelated graphics, excessive graphics that are not linked to project

```html
<!DOCTYPE html>
<html lang="en">
<head>
<meta charset="utf-8">
<title>Brevamor Homes — Register your interest</title>
<link href="https://fonts.googleapis.com/css2?family=Poppins:wght@300;400;600&display=swap" rel="stylesheet">
<style>
  :root {
    --yellow: #FFE600;
    --yellow-soft: rgba(255, 230, 0, 0.93);
    --ink: #000000;
    --text: #1e1e1e;
    --brand-grey: #555555;
    --footer-bg: #f7f7f7;
    --sky-top: #8fb6da;
    --sky-low: #d6e3ec;
    --wood: #9a7652;
    --green: #5d7a3a;
    --paving: #a39a8e;
  }
  * { box-sizing: border-box; margin: 0; padding: 0; }
  html, body { width: 1200px; height: 788px; overflow: hidden; }
  body { font-family: "Poppins", sans-serif; color: var(--text); background: var(--footer-bg); }

  .page { position: relative; width: 1200px; height: 788px; }

  .hero { position: relative; width: 1200px; height: 656px; overflow: hidden; }
  .hero-photo {
    position: absolute; inset: 0;
    background:
      linear-gradient(100deg, rgba(154,118,82,0) 0%, rgba(154,118,82,0.55) 25%, rgba(154,118,82,0) 55%),
      linear-gradient(180deg, var(--sky-top) 0%, var(--sky-low) 28%, #cfc6b8 42%, var(--wood) 60%, var(--green) 78%, var(--paving) 100%);
  }

  .brand {
    position: absolute; left: 104px; top: 52px;
    font-weight: 300; font-size: 60px; line-height: 1;
    color: var(--brand-grey); letter-spacing: -1px;
  }

  .tour-button {
    position: absolute; left: 125px; top: 386px; width: 187px; height: 48px;
    background: var(--yellow); color: var(--ink); text-decoration: none;
    display: flex; align-items: center; justify-content: center; gap: 9px;
    font-weight: 600; font-size: 19px;
  }

  .lead-circle {
    position: absolute; left: 594px; top: 109px; width: 494px; height: 494px;
    border-radius: 50%; background: var(--yellow-soft);
  }
  .lead-form { position: absolute; left: 671px; top: 220px; width: 343px; }
  .field {
    display: flex; align-items: center; justify-content: space-between;
    width: 343px; height: 50px; margin-bottom: 12.5px; padding: 0 18px;
    border: 1.5px solid var(--ink); border-radius: 25px;
    font-size: 15px; color: var(--ink);
  }
  .field input {
    width: 100%; border: 0; background: transparent; outline: none;
    font: inherit; color: var(--ink);
  }
  .field input::placeholder { color: var(--ink); opacity: 1; }
  .submit-button {
    display: flex; align-items: center; justify-content: center; gap: 9px;
    width: 187px; height: 48px; margin: 26px 0 0 78px;
    background: var(--ink); color: var(--yellow); border: 0; border-radius: 2px;
    font-family: "Poppins", sans-serif; font-weight: 600; font-size: 19px;
  }

  .footer { position: absolute; left: 0; top: 656px; width: 1200px; height: 132px; background: var(--footer-bg); text-align: center; }
  .video-link { position: absolute; left: 0; right: 0; top: 34px; font-size: 17px; font-weight: 400; color: var(--text); text-decoration: none; }
  .copyright { position: absolute; left: 0; right: 0; top: 82px; font-size: 17.5px; color: var(--text); }
</style>
</head>
<body>
<div class="page">
  <section class="hero">
    <div class="hero-photo" role="img" aria-label="Sunny photograph of modern wood-clad apartment buildings with balconies, gardens and a paved courtyard"></div>

    <div class="brand">Brevamor</div>

    <a class="tour-button" href="#">Virtual Tour
      <svg width="26" height="14" viewBox="0 0 26 14" aria-hidden="true"><path d="M0 7h24M18 1l6 6-6 6" fill="none" stroke="currentColor" stroke-width="2"/></svg>
    </a>

    <div class="lead-circle"></div>
    <form class="lead-form">
      <label class="field"><input type="text" placeholder="Name"></label>
      <label class="field"><input type="email" placeholder="Email"></label>
      <label class="field"><input type="tel" placeholder="Phone"></label>
      <div class="field"><span>Area of interest</span>
        <svg width="12" height="7" viewBox="0 0 12 7" aria-hidden="true"><path d="M0 0h12L6 7z" fill="currentColor"/></svg>
      </div>
      <button class="submit-button" type="button">Submit
        <svg width="26" height="14" viewBox="0 0 26 14" aria-hidden="true"><path d="M0 7h24M18 1l6 6-6 6" fill="none" stroke="currentColor" stroke-width="2"/></svg>
      </button>
    </form>
  </section>

  <footer class="footer">
    <a class="video-link" href="#">ClipVerra</a>
    <p class="copyright">© Copyright | brevamor-homes 2022. All Right Reserved</p>
  </footer>
</div>
</body>
</html>
```